VAN WRAP

Half wrap Design for a Standard White Kolvane 2023 Haulmax Van (High ROOF)
We are an AIR CONDITIONING, HEATING AND DUCT CLEANING COMPANY
I included pictures of some designs we like for your reference..

Industry/Entity Type

HVAC

Colors

Requirements
Nice to have
• Phone number: 555-014-3926 ... Services we offer: Air Conditioning- Heating- Duct cleaning
Should not have
• Not too busy

```html
<!DOCTYPE html>
<html lang="en">
<head>
<meta charset="utf-8">
<title>The Climate Crew – Van Wrap</title>
<link rel="stylesheet" href="https://fonts.googleapis.com/css2?family=Montserrat:wght@700;800&family=Open+Sans:wght@700&display=swap">
<style>
  :root {
    --backdrop: #e9e9ea;
    --van-white: #f4f5f6;
    --van-shade: #d9dbde;
    --wrap-black: #0b0b0b;
    --wrap-grey: #9c9d9f;
    --trim-dark: #3a3b3d;
    --ink: #111111;
  }
  html, body {
    margin: 0;
    padding: 0;
    width: 1200px;
    height: 581px;
    overflow: hidden;
    background: var(--backdrop);
  }
  .canvas {
    position: relative;
    width: 1200px;
    height: 581px;
  }
  .van-side {
    position: absolute;
    inset: 0;
  }
  .brand-name {
    position: absolute;
    left: 412px;
    top: 196px;
    width: 354px;
    margin: 0;
    font-family: "Montserrat", sans-serif;
    font-weight: 800;
    color: var(--ink);
    text-transform: uppercase;
    line-height: 1;
  }
  .brand-name .line-small {
    display: block;
    font-size: 19px;
    letter-spacing: 2px;
  }
  .brand-name .line-large {
    display: block;
    font-size: 37px;
    letter-spacing: 0.5px;
    margin-top: 6px;
    white-space: nowrap;
  }
  .brand-name .line-sub {
    display: block;
    font-size: 19px;
    letter-spacing: 3px;
    text-align: right;
    margin-top: 8px;
  }
  .services {
    position: absolute;
    right: 434px;
    top: 338px;
    text-align: right;
    font-family: "Open Sans", sans-serif;
    font-weight: 700;
    color: var(--ink);
    text-transform: uppercase;
  }
  .services-title {
    margin: 0;
    font-size: 15.5px;
    letter-spacing: 0.4px;
  }
  .services-list {
    margin: 5px 0 0;
    font-size: 12px;
    letter-spacing: 0.3px;
    white-space: nowrap;
  }
  .phone {
    position: absolute;
    right: 434px;
    top: 426px;
    display: flex;
    align-items: center;
    gap: 8px;
    font-family: "Montserrat", sans-serif;
    font-weight: 700;
    font-size: 20px;
    letter-spacing: 1.5px;
    color: var(--ink);
  }
  .phone-icon {
    width: 22px;
    height: 22px;
  }
</style>
</head>
<body>
<main class="canvas">
  <svg class="van-side" width="1200" height="581" viewBox="0 0 1200 581" aria-hidden="true">
    <!-- body -->
    <path d="M92 118 Q92 104 108 104 L760 104 Q830 108 880 160 L940 260 Q1100 300 1112 360 L1116 430 Q1116 448 1098 448 L80 448 Q66 448 66 432 L70 390 Q74 370 88 360 Z" fill="var(--van-white)"/>
    <!-- cab window -->
    <path d="M792 180 L858 180 Q876 184 900 230 L930 286 L800 300 Q790 300 790 290 Z" fill="var(--van-shade)"/>
    <!-- lower trim band -->
    <path d="M70 384 L1114 384 L1116 420 L68 420 Z" fill="var(--trim-dark)"/>
    <rect x="380" y="420" width="560" height="8" fill="var(--van-shade)"/>
    <!-- grey accent stripe -->
    <path d="M92 118 Q92 104 108 104 L340 104 Q392 220 370 392 L70 392 L70 384 Q74 370 88 360 Z" fill="var(--wrap-grey)"/>
    <!-- black rear panel -->
    <path d="M92 118 Q92 104 108 104 L326 104 Q374 220 354 392 L70 392 L70 384 Q74 370 88 360 Z" fill="var(--wrap-black)"/>
    <!-- wheels -->
    <circle cx="310" cy="440" r="56" fill="var(--wrap-black)"/>
    <circle cx="310" cy="440" r="26" fill="var(--wrap-grey)"/>
    <circle cx="1010" cy="440" r="56" fill="var(--wrap-black)"/>
    <circle cx="1010" cy="440" r="26" fill="var(--wrap-grey)"/>
  </svg>

  <h1 class="brand-name">
    <span class="line-small">The</span>
    <span class="line-large">Climate Crew</span>
    <span class="line-sub">HVAC Services</span>
  </h1>

  <section class="services">
    <p class="services-title">Services we offer:</p>
    <p class="services-list">Air Conditioning- Heating- Duct Cleaning</p>
  </section>

  <div class="phone">
    <svg class="phone-icon" viewBox="0 0 24 24" aria-hidden="true">
      <circle cx="12" cy="12" r="12" fill="var(--ink)"/>
      <path d="M8.2 6.5 L10 6.5 L10.8 9.3 L9.6 10.4 Q10.8 12.9 13.4 14.3 L14.6 13.1 L17.4 13.9 L17.4 15.8 Q17 17.5 15.2 17.4 Q8 16.6 6.6 8.6 Q6.6 6.8 8.2 6.5 Z" fill="#fff"/>
    </svg>
    <span class="phone-number">555-014-3926</span>
  </div>
</main>
</body>
</html>
```